Labels design for a a range of food products

We are looking for labels design for a range of food product. The design should be the same for all the label with brown/black background and gold and white wording like the one attached.
The size and the content of the label will change depending on the different products.
I have also attached the logo to be used which is the logo "CORVANE" Telmora. You shall be using the black and gold version. Brighter/shining gold is better.
The first label to be designed is the one related a plastic tray like the one Cappelletti" file: IMG_20151231_021838
The second label to be designed is the one related to a bottle like the one "Olive Oil" file; IMG_20151231_021651
The third label to be designed is the one related to a jar like the one "Olive Taggiasche" file: IMG_20151231_021531 and IMG_20151231_021549
The fourth label to be designed is the one related to bag like the one IMG_20151231_021506
The fifth label to be designed is the one related to the bottle. IMG_20151231_021426_panorama
This files are only samples. I have attached a file excel "Texts for Labels" in which you will find the text to be applied for the labels.
In order to decide the best design a front and a back label should be provided.

Food Consumers

Product

• Front and Back Label
• Some pictures of the product on the label would be nice to have to recall what is inside.

```html
<!DOCTYPE html>
<html lang="it">
<head>
<meta charset="utf-8">
<title>Olio Extravergine d'Oliva DOP – Etichetta frontale</title>
<link href="https://fonts.googleapis.com/css2?family=Great+Vibes&family=Roboto:wght@400;500;700&display=swap" rel="stylesheet">
<style>
  :root {
    --page-bg: #f7f7f5;
    --label-bg: #0a0a0b;
    --label-bg-low: #141414;
    --gold: #e8b84a;
    --gold-bright: #f3cf6a;
    --white: #f2f2f2;
    --leaf: #7e9f5a;
    --leaf-light: #b7c98a;
  }
  * { margin: 0; padding: 0; box-sizing: border-box; }
  html, body {
    width: 948px;
    height: 1200px;
    overflow: hidden;
    background: var(--page-bg);
  }
  .label {
    position: absolute;
    left: 314px;
    top: 60px;
    width: 320px;
    height: 1080px;
    background: linear-gradient(180deg, var(--label-bg) 0%, var(--label-bg) 70%, var(--label-bg-low) 100%);
    color: var(--white);
    font-family: "Roboto", Arial, sans-serif;
    text-align: center;
  }
  .category {
    position: absolute;
    top: 36px;
    left: 0;
    width: 100%;
    color: var(--gold);
    font-size: 20px;
    line-height: 26px;
    font-weight: 400;
  }
  .product-name {
    position: absolute;
    top: 128px;
    left: 0;
    width: 100%;
    font-family: "Great Vibes", cursive;
    color: var(--gold);
    font-weight: 400;
    font-size: 56px;
    line-height: 80px;
  }
  .product-name .line-one { display: block; padding-right: 24px; }
  .product-name .line-two { display: block; }
  .process {
    position: absolute;
    top: 318px;
    left: 0;
    width: 100%;
    color: var(--gold);
    font-size: 19px;
  }
  .olive-branch {
    position: absolute;
    top: 380px;
    left: 30px;
    width: 210px;
    height: 246px;
    margin-left: 20px;
    border-radius: 40% 50% 45% 55%;
    background: radial-gradient(ellipse at 55% 50%, var(--leaf-light) 0%, var(--leaf) 45%, rgba(10,10,11,0) 72%);
  }
  .description {
    position: absolute;
    top: 678px;
    left: 0;
    width: 100%;
    font-size: 14px;
    line-height: 27px;
    color: var(--white);
  }
  .brand {
    position: absolute;
    top: 880px;
    left: 0;
    width: 100%;
    display: flex;
    flex-direction: column;
    align-items: center;
  }
  .brand-dot {
    width: 130px;
    height: 130px;
    border-radius: 50%;
    background: radial-gradient(circle at 40% 35%, var(--gold-bright), var(--gold) 70%);
  }
  .brand-name {
    margin-top: 10px;
    font-family: "Roboto", Arial, sans-serif;
    font-weight: 700;
    font-size: 22px;
    line-height: 26px;
    color: var(--gold-bright);
  }
</style>
</head>
<body>
  <main class="label">
    <p class="category">Olio Extravergine<br>d’Oliva DOP</p>
    <h1 class="product-name">
      <span class="line-one">Collina</span>
      <span class="line-two">di Sarvento</span>
    </h1>
    <p class="process">- estratto a freddo -</p>
    <div class="olive-branch" role="img" aria-label="Illustrazione di un ramo d'ulivo con olive verdi e foglie"></div>
    <p class="description">
      Olio d’ Oliva di categoria<br>
      superiore ottenuto<br>
      direttamente dalle olive<br>
      e unicamente mediante<br>
      procedimenti meccanici
    </p>
    <div class="brand">
      <span class="brand-dot" aria-hidden="true"></span>
      <span class="brand-name">CORVANE<br>Telmora</span>
    </div>
  </main>
</body>
</html>
```